Business Card Design Needed

Business car design required, logo will be supplied.

Brambleford Power Surveyors are looking to become the leading provider of energy performance certificates to estate agents, landlords and home owners in the Yorkshire region of the UK.

The business card must be double sided and professional looking. Estate agents receive hundreds of cards from contractors and our card must stand out.

I require a two sided business card that is clean, modern and created by a designer that can think outside of the box.

Brand colours can be supplied .

Please ask if you have any questions.

Target Market(s)

Estate agents, landlords and property owners

Industry/Entity Type

Property - estate agency - energy consultants

Contact Information for Business Card

Tomas Rendell - Energy Assessor - 07311642705 - www.BramblefordPSV.co.uk - info@bramblefordpsv.co.uk

Font styles to use
Serif
Sans Serif

Colors
00AB8E
00BBA5
67D7C9
C6EFE9
E9F9F6

Requirements
Must have
• Use the provided logo, clean, professional and stand out from the crowd
Nice to have
• Clever use of text, spacing and brand colours
Should not have
• Clip art

```html
<!DOCTYPE html>
<html lang="en">
<head>
<meta charset="utf-8">
<title>Brambleford Power Surveyors – Business Card</title>
<link href="https://fonts.googleapis.com/css2?family=Open+Sans:wght@400;600;700&display=swap" rel="stylesheet">
<style>
  :root {
    --bg: #2a2d31;
    --blue-deep: #135d9c;
    --blue: #1a74b6;
    --lime: #b6d22a;
    --white: #ffffff;
    --text-soft: #e6eef6;
    --navy-text: #1d5f9e;
  }
  * { margin: 0; padding: 0; box-sizing: border-box; }
  html, body {
    width: 1200px; height: 900px; overflow: hidden;
    background: var(--bg);
    font-family: "Open Sans", Arial, sans-serif;
  }
  .stage { position: relative; width: 1200px; height: 900px; }

  .card {
    position: absolute;
    border-radius: 22px;
    overflow: hidden;
    background: linear-gradient(135deg, var(--blue-deep), var(--blue));
    box-shadow: 0 18px 40px rgba(0,0,0,.45);
  }

  /* Front: portrait */
  .card-front { left: 110px; top: 140px; width: 380px; height: 620px; }
  .card-front .arc { position: absolute; inset: 0; }
  .contact { position: absolute; left: 34px; top: 40px; color: var(--text-soft); }
  .contact .name {
    color: var(--lime); font-weight: 700; font-size: 25px;
    text-transform: uppercase; letter-spacing: .3px;
  }
  .contact .role { font-size: 15px; margin-top: 2px; }
  .contact .rule { width: 14px; height: 2px; background: var(--lime); margin: 12px 0 12px; }
  .contact ul { list-style: none; font-size: 15px; line-height: 1.75; }
  .contact li { display: flex; align-items: center; gap: 8px; }
  .contact svg { width: 13px; height: 13px; flex: none; }

  .front-mark {
    position: absolute; left: 122px; top: 430px; width: 220px;
    display: flex; align-items: center; gap: 10px;
  }
  .mark-dot {
    width: 30px; height: 30px; border-radius: 50%; flex: none;
    border: 4px solid var(--lime);
  }
  .front-mark .brand-name {
    color: var(--navy-text); font-size: 19px; font-weight: 600;
    text-transform: uppercase; letter-spacing: 1px; line-height: 1.15;
  }

  /* Back: landscape */
  .card-back { left: 550px; top: 240px; width: 620px; height: 380px; }
  .back-mark {
    position: absolute; left: 0; right: 0; top: 0; bottom: 0;
    display: flex; align-items: center; justify-content: center; gap: 18px;
  }
  .back-mark .mark-dot { width: 52px; height: 52px; border-width: 6px; }
  .back-mark .brand-name {
    color: var(--white); font-size: 30px; font-weight: 400;
    text-transform: uppercase; letter-spacing: 2px; line-height: 1.15;
  }
</style>
</head>
<body>
<main class="stage">

  <section class="card card-front" aria-label="Card front">
    <svg class="arc" viewBox="0 0 380 620" aria-hidden="true">
      <circle cx="330" cy="560" r="275" fill="var(--white)" stroke="var(--lime)" stroke-width="5"/>
    </svg>
    <div class="contact">
      <p class="name">Tomas Rendell</p>
      <p class="role">Energy Assessor</p>
      <div class="rule"></div>
      <ul>
        <li>
          <svg viewBox="0 0 16 16"><path fill="var(--lime)" d="M3 1h3l1.5 4-2 1.3a9 9 0 0 0 4.2 4.2L11 8.5l4 1.5v3a2 2 0 0 1-2 2A12 12 0 0 1 1 3a2 2 0 0 1 2-2z"/></svg>
          07311642705
        </li>
        <li>
          <svg viewBox="0 0 16 16"><rect x="1" y="3" width="14" height="10" rx="1" fill="var(--lime)"/><path d="M1.5 4l6.5 5 6.5-5" fill="none" stroke="var(--blue-deep)" stroke-width="1.4"/></svg>
          info@bramblefordpsv.co.uk
        </li>
        <li>
          <svg viewBox="0 0 16 16"><circle cx="8" cy="8" r="7" fill="var(--lime)"/><path d="M1 8h14M8 1c-3 3.5-3 10.5 0 14M8 1c3 3.5 3 10.5 0 14" fill="none" stroke="var(--blue-deep)" stroke-width="1"/></svg>
          www.BramblefordPSV.co.uk
        </li>
      </ul>
    </div>
    <div class="front-mark">
      <span class="mark-dot"></span>
      <span class="brand-name">Brambleford Power Surveyors</span>
    </div>
  </section>

  <section class="card card-back" aria-label="Card back">
    <div class="back-mark">
      <span class="mark-dot"></span>
      <span class="brand-name">Brambleford<br>Power Surveyors</span>
    </div>
  </section>

</main>
</body>
</html>
```